Brightwater Charity Ball Poster

We are looking for a poster for our upcoming event, "Brightwater Charity Ball" - a sit down dinner formal event hosted by our university club, OKRU.
Usually we source designs internally from our committee (even if they aren't the most amazing quality), however this time round we have no one available to do it as everyone is a volunteer.
The event's theme is 'winter wonderland', based around the snowy forests you see in Veltmoor or Crown of Ashes (neither of these specific things are the theme however). Our venue is a clear-roof marque in a space surrounded by very tall pine trees giving off the forest vibe, and there are festoons strung between the trees so this is an element of warm light amongst the forest, perhaps a building or village tucked away in the forest.
The poster is for printing out at A3 size, and we will also need to create a Facebook event cover photo and other marketing graphics from the original poster files so some flexibility in the design and original files are required.
Things that need to be included on the poster :
---Event details
Brightwater Charity Ball
Saturday 12th August
7pm – midnight
Halberd Auditorium, KPC
Tables of 10
Members - $140
Non members - $150
All profits donated to Stride for Hope
---- Extra info and images (can be at the bottom, in corners etc,)
18+ ID required | Drink Responsibly
OKRU Logo
KPC Union Logo
(these logos may be changed to black and white if need be)
Example images of styles, colours and the sort of landscape we want for the poster can be found in the document attached.

```html
<!DOCTYPE html>
<html lang="en">
<head>
<meta charset="utf-8">
<title>Brightwater Charity Ball</title>
<link href="https://fonts.googleapis.com/css2?family=Yesteryear&family=Kreon:wght@400;500&display=swap" rel="stylesheet">
<style>
  :root {
    --ink: #363a58;
    --white: #ffffff;
    --sky-gold: #f3d9a4;
    --sky-cream: #f8ecd2;
    --haze-rose: #d9b3ae;
    --mountain-mauve: #9c8294;
    --forest-dusk: #5c5268;
    --lake-plum: #6e5a78;
    --lake-rose: #c99a97;
    --shore-cream: #f1dcc4;
    --script: "Yesteryear", cursive;
    --text: "Kreon", serif;
  }
  html, body {
    margin: 0;
    padding: 0;
    overflow: hidden;
  }
  .poster {
    position: relative;
    width: 849px;
    height: 1200px;
    overflow: hidden;
    color: var(--ink);
    font-family: var(--text);
  }
  .landscape {
    position: absolute;
    inset: 0;
    background:
      radial-gradient(ellipse 70% 30% at 20% 5%, var(--sky-cream), transparent 70%),
      linear-gradient(180deg,
        var(--sky-gold) 0%,
        var(--sky-cream) 18%,
        var(--haze-rose) 32%,
        var(--mountain-mauve) 48%,
        var(--forest-dusk) 60%,
        var(--lake-plum) 66%,
        var(--lake-rose) 78%,
        var(--mountain-mauve) 86%,
        var(--shore-cream) 100%);
  }
  .emblem-circle {
    position: absolute;
    left: 40px;
    top: 42px;
    width: 762px;
    height: 762px;
    border-radius: 50%;
    border: 4px solid var(--white);
    background: radial-gradient(circle at 50% 40%, rgba(255,255,255,0.62), rgba(255,255,255,0.38));
  }
  .line {
    position: absolute;
    left: 0;
    width: 849px;
    text-align: center;
    margin: 0;
    white-space: nowrap;
  }
  .title-top {
    top: 150px;
    font-family: var(--script);
    font-size: 100px;
    line-height: 1;
  }
  .title-bottom {
    top: 262px;
    font-family: var(--script);
    font-size: 128px;
    line-height: 1;
  }
  .event-date { top: 440px; font-size: 37px; }
  .event-venue { top: 494px; font-size: 35px; }
  .tables { top: 574px; font-size: 37px; }
  .price-members { top: 628px; font-size: 30px; font-weight: 500; }
  .price-guests { top: 670px; font-size: 30px; font-weight: 500; }
  .donation-lead {
    top: 830px;
    font-family: var(--script);
    font-size: 32px;
    color: #22243a;
  }
  .charity-name {
    top: 872px;
    font-family: var(--script);
    font-size: 72px;
    color: #22243a;
  }
  .age-notice {
    top: 1046px;
    font-size: 16px;
    color: var(--white);
  }
  .partners {
    position: absolute;
    top: 1112px;
    left: 0;
    width: 849px;
    display: flex;
    justify-content: center;
    gap: 70px;
    align-items: center;
  }
  .partner {
    display: flex;
    align-items: center;
    gap: 10px;
    font-family: var(--text);
    font-size: 26px;
    font-weight: 500;
    color: var(--ink);
  }
  .partner-mark {
    width: 26px;
    height: 26px;
    background: var(--ink);
  }
  .partner-mark.round { border-radius: 50%; }
</style>
</head>
<body>
<main class="poster">
  <div class="landscape" role="img" aria-label="Photograph of snow-capped mountains above a still alpine lake with pine forest, under a warm golden sky, reflected in the water"></div>
  <div class="emblem-circle"></div>

  <h1 class="line title-top">Brightwater</h1>
  <p class="line title-bottom">Charity Ball</p>

  <p class="line event-date">Saturday 12th August | 7pm – midnight</p>
  <p class="line event-venue">Halberd Auditorium, KPC</p>

  <p class="line tables">Tables of 10</p>
  <p class="line price-members">Members - $140</p>
  <p class="line price-guests">Non Members - $150</p>

  <p class="line donation-lead">All profits donated to</p>
  <p class="line charity-name">Stride for Hope</p>

  <p class="line age-notice">18+ ID required | Drink Responsibly</p>

  <div class="partners">
    <div class="partner"><span class="partner-mark round"></span>OKRU</div>
    <div class="partner"><span class="partner-mark"></span>KPC Union</div>
  </div>
</main>
</body>
</html>
```